3 Politically Incorrect Greeting Cards

I would like to see some clean, colorful, and modern designs for 3 "politically incorrect" greeting cards aimed at young, single, successful women. I would like them to say:

Card 1: " Congratulations on not marrying the wrong person"
Card 2: " Congratulations on buying a house without a husband"
Card 3: " Thank you for not forgetting about me now that you have a boyfriend"

My initial thought was to have a white background with simple black writing, but I think a colorful background with a white text box in the middle might be more appropriate. I can't imagine the cards having any images/icons on them, but I'm open to suggestions if you think it would improve on the design. You guys are likely more creative than I am.

I've included a couple pics of looks I like - but like I said - I'm open to suggestions and what I like may not be appropriate for these cards. All the cards can have a similar esthetic or theme (maybe the same fonts but different colors or different color florals in each) or they can be completely different.

Target Market(s)

Young, single, successful women mid-20s to mid 40's.

Font styles to use
Serif
Sans Serif
Other font styles liked:
• Watercolour lettering maybe

Colors

Designer to choose colors to be used in the design.

Requirements
Must have
• Clean, colorful, bright, professional looking. The right tone for the message.
• I think the message is bold so the writing and colors have to be as well. I have included examples of ideas I like.
Nice to have
• Images, illustrations, icons, maybe patterns or some decorative details. Something to make the card more interesting than just the words (like the blue background with black letters one I made). I like a bright pattern with a white box in the center with the text.
Should not have
• Special effects, galaxy pictures, ugly images, bland colors.

```html
<!DOCTYPE html>
<html lang="en">
<head>
<meta charset="utf-8">
<title>Congratulations on not marrying the wrong person – Greeting Card</title>
<link rel="stylesheet" href="https://fonts.googleapis.com/css2?family=Short+Stack&display=swap">
<style>
  :root {
    --card-width: 857px;
    --card-height: 1200px;
    --floral-orange: #f2a23a;
    --floral-amber: #f7b733;
    --floral-teal: #4fdcc0;
    --floral-pink: #e23fb4;
    --floral-lime: #b5e63c;
    --badge-white: #ffffff;
    --ink: #1a1a1a;
  }

  * { margin: 0; padding: 0; box-sizing: border-box; }

  html, body {
    width: var(--card-width);
    height: var(--card-height);
    overflow: hidden;
    background: #ffffff;
  }

  .greeting-card {
    position: relative;
    width: var(--card-width);
    height: var(--card-height);
    overflow: hidden;
  }

  .floral-pattern {
    position: absolute;
    inset: 0;
    background:
      radial-gradient(circle at 15% 12%, var(--floral-teal) 0, transparent 28%),
      radial-gradient(circle at 85% 20%, var(--floral-pink) 0, transparent 26%),
      radial-gradient(circle at 10% 70%, var(--floral-pink) 0, transparent 24%),
      radial-gradient(circle at 90% 75%, var(--floral-teal) 0, transparent 26%),
      radial-gradient(circle at 50% 95%, var(--floral-lime) 0, transparent 25%),
      linear-gradient(160deg, var(--floral-amber) 0%, var(--floral-orange) 50%, var(--floral-amber) 100%);
  }

  .message-badge {
    position: absolute;
    left: 128px;
    top: 300px;
    width: 600px;
    height: 600px;
    border-radius: 50%;
    background: var(--badge-white);
    box-shadow: 6px 10px 18px rgba(0, 0, 0, 0.28);
    display: flex;
    align-items: center;
    justify-content: center;
  }

  .message-text {
    font-family: "Short Stack", "Comic Sans MS", cursive;
    font-size: 45px;
    line-height: 72px;
    color: var(--ink);
    text-align: center;
    margin-top: -10px;
    letter-spacing: 0.5px;
  }
</style>
</head>
<body>
  <main class="greeting-card">
    <div class="floral-pattern" role="img" aria-label="Bright doodle floral pattern of orange, teal, pink and yellow flowers with hearts and leaves"></div>
    <div class="message-badge">
      <p class="message-text">Congratulations<br>on not<br>marrying the<br>wrong person</p>
    </div>
  </main>
</body>
</html>
```